COVID-19 Related Signage for Hotel

Need to create new COVID-19 related signage utilizing our brand assets. Please use screenshots for copy/direction. essentially duplicate the screenshots but with our logo/branding.

All brand assets have been uploaded and examples of signage content. Pictures are not necessary but you can add them if you want similar to the examples attached.

Sign requirements

sign 1. Text "Hand Sanitizer Station" can add graphic
sign 2. Text "Protect Yourself" duplicate copy in the attached pictures
sign 3. Text "Face Mask Required" can add graphic
sign 4. Text "Face Covering Do's and Don'ts with text from "Face-covering checklist.jpg" REMOVE BWR logo or website or 3 face mask graphics
sign 5. Text "Maintain 6 Foot Distance" This sign will be printed and placed on the ground for guests to know where to stand in queue. Would prefer a circular Design. sign 6. Text "Wet, Lather, Scrub, Rinse, Dry" similar to screenshots attached.

ALL signs should have same look and feel throughout utilizing our brand graphics, logo, colors, and guidelines.

Target Market(s)

Hotel Guests

Industry/Entity Type

Hotel

Font styles to use
Sans Serif

Requirements
Must have
• Cohesive, unified branding look and feel

Should not have
• any use of the word "COVID-19" or Coronavirus.

```html
<!DOCTYPE html>
<html lang="en">
<head>
<meta charset="utf-8">
<title>Guest Safety Signage – Ridgeview Lodge</title>
<link href="https://fonts.googleapis.com/css2?family=Oswald:wght@300;400&display=swap" rel="stylesheet">
<style>
  :root{
    --orange:#f3892f;
    --charcoal:#555658;
    --slate:#5d5d5f;
    --paper:#f8f8f8;
    --backdrop:#e4e4e4;
    --white:#ffffff;
    --tick:#2aa24a;
    --cross:#e02020;
  }
  *{box-sizing:border-box;margin:0;padding:0}
  html,body{width:1200px;height:1059px;overflow:hidden;background:var(--backdrop);font-family:"Oswald",sans-serif}
  .stage{position:relative;width:1200px;height:1059px}
  .floor-badge{position:absolute;top:182px;width:202px;height:202px}
  .sign{position:absolute;width:445px;height:222px;background:var(--paper);overflow:hidden}
  .sign::after{content:"";position:absolute;left:0;right:0;bottom:0;height:9px;background:var(--orange)}
  .sign-title{position:absolute;left:23px;color:var(--charcoal);font-weight:400;letter-spacing:-0.5px}
  .brand-mark{position:absolute;left:368px;top:21px;width:52px;height:52px;border-radius:50%;background:var(--orange);
    display:flex;align-items:center;justify-content:center;color:var(--white);font-weight:300;font-size:10px;line-height:1}
  .art-disc{position:absolute;border-radius:50%;background:var(--orange);box-shadow:0 0 0 3px var(--paper),0 0 0 5px var(--orange)}

  /* sanitizing station */
  .station{left:137px;top:423px}
  .station .sign-title{top:12px;font-size:58px;line-height:61px}
  .station .art-disc{left:251px;top:60px;width:130px;height:130px}

  /* hand washing steps */
  .steps{left:602px;top:423px}
  .step{position:absolute;bottom:0;width:89px;color:var(--white);font-size:14px;line-height:16px;padding:16px 8px 0 9px}
  .step.orange{background:var(--orange)}
  .step.slate{background:var(--slate)}
  .step-label{position:absolute;font-size:33px;line-height:1;font-weight:400}
  .step-label.orange{color:var(--orange)}
  .step-label.slate{color:var(--charcoal)}
  .steps::after{display:none}

  /* face covering */
  .covering{left:137px;top:665px}
  .covering .sign-title{top:12px;font-size:46px;line-height:54px}
  .rule-bar{position:absolute;top:128px;width:143px;height:18px;background:var(--orange);color:var(--white);font-size:17px;line-height:18px;padding-left:6px}
  .rule-bar.do{left:23px}
  .rule-bar.dont{left:208px}
  .bar-arrows{position:absolute;left:178px;top:131px}
  .rule-list{position:absolute;top:153px;list-style:none;font-size:7.5px;line-height:13px;color:var(--charcoal);font-weight:300}
  .rule-list.do{left:24px}
  .rule-list.dont{left:217px}
  .rule-list li{padding-left:15px;position:relative}
  .rule-list li.cont{padding-left:15px}
  .rule-list svg{position:absolute;left:0;top:3px}

  /* face mask */
  .mask{left:602px;top:665px}
  .mask .sign-title{top:12px;font-size:60px;line-height:62px}
  .mask .art-disc{left:254px;top:66px;width:130px;height:130px}
</style>
</head>
<body>
<main class="stage">

  <svg width="0" height="0" style="position:absolute" aria-hidden="true">
    <defs>
      <path id="arc-top" d="M 22 100 A 78 78 0 0 1 178 100"/>
      <path id="arc-bottom" d="M 12 100 A 88 88 0 0 0 188 100"/>
      <symbol id="distance-badge" viewBox="0 0 202 202">
        <g transform="translate(1 1)">
          <circle cx="100" cy="100" r="100" fill="#f3892f"/>
          <circle cx="100" cy="100" r="97" fill="none" stroke="#fff" stroke-width="1"/>
          <circle cx="100" cy="100" r="68" fill="none" stroke="#fff" stroke-width="1.2"/>
          <text font-family="Oswald, sans-serif" font-size="21" fill="#fff" letter-spacing="6">
            <textPath href="#arc-top" startOffset="50%" text-anchor="middle">MAINTAIN</textPath>
          </text>
          <text font-family="Oswald, sans-serif" font-size="21" fill="#fff" letter-spacing="3">
            <textPath href="#arc-bottom" startOffset="50%" text-anchor="middle">FOOT DISTANCE</textPath>
          </text>
          <text x="100" y="143" text-anchor="middle" font-family="Oswald, sans-serif" font-size="122" fill="#fff">6</text>
          <g fill="#fff">
            <path d="M6 94 l6 5 l-6 5z"/><path d="M14 94 l6 5 l-6 5z"/><path d="M22 94 l6 5 l-6 5z"/>
          </g>
          <circle cx="150" cy="99" r="18" fill="none" stroke="#fff" stroke-width="0.8"/>
          <text x="150" y="102" text-anchor="middle" font-family="Oswald, sans-serif" font-weight="300" font-size="7.5" fill="#fff">Ridgeview</text>
        </g>
      </symbol>
    </defs>
  </svg>

  <svg class="floor-badge" style="left:147px" role="img" aria-label="Maintain 6 foot distance"><use href="#distance-badge"/></svg>
  <svg class="floor-badge" style="left:367px" role="img" aria-label="Maintain 6 foot distance"><use href="#distance-badge"/></svg>
  <svg class="floor-badge" style="left:611px" role="img" aria-label="Maintain 6 foot distance"><use href="#distance-badge"/></svg>
  <svg class="floor-badge" style="left:831px" role="img" aria-label="Maintain 6 foot distance"><use href="#distance-badge"/></svg>

  <section class="sign station">
    <h1 class="sign-title">Hand<br>Sanitizing<br>Station</h1>
    <div class="brand-mark">Ridgeview</div>
    <div class="art-disc" role="img" aria-label="Icon of a hand under a sanitizer pump bottle"></div>
  </section>

  <section class="sign steps">
    <div class="step orange" style="left:0;height:181px">Wash with clean, running water</div>
    <div class="step slate" style="left:89px;height:150px;padding-top:18px">Lather with soap, in between fingers, under nails &amp; all over hands</div>
    <div class="step orange" style="left:178px;height:122px;padding-top:8px">Scrub for at least 20 seconds</div>
    <div class="step slate" style="left:267px;height:91px;padding-top:14px">Rinse with clean, running water</div>
    <div class="step orange" style="left:356px;height:62px;padding-top:8px;width:89px">Dry with a clean towel or air dry</div>
    <span class="step-label orange" style="left:19px;top:8px">WET</span>
    <span class="step-label slate" style="left:91px;top:40px">LATHER</span>
    <span class="step-label orange" style="left:184px;top:69px">SCRUB</span>
    <span class="step-label slate" style="left:278px;top:99px">RINSE</span>
    <span class="step-label orange" style="left:375px;top:129px">DRY</span>
    <div class="brand-mark" style="left:368px;top:22px">Ridgeview</div>
  </section>

  <section class="sign covering">
    <h1 class="sign-title">Face Covering<br>Do’s and Don’ts:</h1>
    <div class="brand-mark">Ridgeview</div>
    <div class="rule-bar do">Do:</div>
    <svg class="bar-arrows" width="22" height="12" aria-hidden="true">
      <path fill="#f3892f" d="M0 1 l6 5 l-6 5z M8 1 l6 5 l-6 5z M16 1 l6 5 l-6 5z"/>
    </svg>
    <div class="rule-bar dont">Don’t:</div>
    <ul class="rule-list do">
      <li><svg width="10" height="7"><path d="M1 4 l3 2.5 l5-5.5" fill="none" stroke="#2aa24a" stroke-width="1.2"/></svg>Make sure you can breathe through it</li>
      <li><svg width="10" height="7"><path d="M1 4 l3 2.5 l5-5.5" fill="none" stroke="#2aa24a" stroke-width="1.2"/></svg>Wear it whenever going out in public</li>
      <li><svg width="10" height="7"><path d="M1 4 l3 2.5 l5-5.5" fill="none" stroke="#2aa24a" stroke-width="1.2"/></svg>Make sure it covers your nose and mouth</li>
      <li class="cont">wash after using</li>
    </ul>
    <ul class="rule-list dont">
      <li><svg width="8" height="8"><path d="M1 1 l6 6 M7 1 l-6 6" stroke="#e02020" stroke-width="1.3"/></svg>Use if under two years old</li>
      <li><svg width="8" height="8"><path d="M1 1 l6 6 M7 1 l-6 6" stroke="#e02020" stroke-width="1.3"/></svg>Use surgical masks or other PPE intended</li>
      <li class="cont">for healthcare workers</li>
    </ul>
  </section>

  <section class="sign mask">
    <h1 class="sign-title">Face<br>Mask<br>Required</h1>
    <div class="brand-mark">Ridgeview</div>
    <div class="art-disc" role="img" aria-label="Illustration of a guest wearing a face mask"></div>
  </section>

</main>
</body>
</html>
```